Flyer-Design für Anbieter von Produkten für Gewichtsmanagement
Zielgruppe
Wir bieten Produkte für ganz einfaches und gesundes Abnehmen bzw. Gewichtsmanagement. Unsere Zielgruppe sind nahezu alle Menschen.
Aufgabenstellung
Optische Anlehnung an einen bestehenden Ratgeber. Die dritte Seite in PDF zeigt die Titelseite des Ratgebers. Die hochgeladenen Fotos sind aus dem Ratgeber.Grober Entwurf besteht bereits ( Seite 1+2 der PDF) . Der Flyer soll 1/3 A3 oder 1/2 A4 sein

```html
<!DOCTYPE html>
<html lang="de">
<head>
<meta charset="utf-8">
<title>Flyer – Gewichtsmanagement</title>
<link href="https://fonts.googleapis.com/css2?family=Urbanist:wght@400;500;800&family=Mr+Dafoe&display=swap" rel="stylesheet">
<style>
  :root {
    --orange: #f0860c;
    --orange-deep: #e0701a;
    --orange-light: #f7a445;
    --white: #ffffff;
    --page: #ffffff;
  }
  * { margin: 0; padding: 0; box-sizing: border-box; }
  html, body { width: 1145px; height: 1200px; overflow: hidden; background: var(--page); }
  body { position: relative; font-family: "Urbanist", sans-serif; color: var(--white); }

  .flyer-side { position: absolute; left: 86px; width: 973px; height: 486px; overflow: hidden; }
  .flyer-side--front { top: 82px; }
  .flyer-side--back { top: 632px; }
  .side-bg { position: absolute; inset: 0; width: 100%; height: 100%; }

  .abs { position: absolute; white-space: nowrap; }
  .script { font-family: "Mr Dafoe", cursive; font-weight: 400; line-height: 1; }
  .url-box {
    position: absolute; background: var(--white); color: var(--orange);
    font-weight: 800; display: flex; align-items: center; justify-content: center;
    letter-spacing: 0.3px;
  }
  .checklist { position: absolute; list-style: none; }
  .checklist li { display: flex; align-items: center; white-space: nowrap; }
  .tick { flex: none; }

  /* front */
  .tagline { right: 53px; top: 78px; font-size: 40px; }
  .front-url { left: 501px; top: 121px; width: 430px; height: 43px; font-size: 31px; }
  .front-guarantee { right: 66px; top: 172px; font-size: 34px; }
  .front-list { left: 703px; top: 238px; font-size: 20.5px; font-weight: 400; }
  .front-list li { height: 29px; gap: 10px; }
  .hotline { left: 650px; top: 418px; font-size: 23px; font-weight: 400; }

  /* back */
  .intro { left: 46px; top: 41px; font-size: 20px; line-height: 24px; font-weight: 400; }
  .invite { right: 405px; top: 102px; font-size: 20px; line-height: 24px; text-align: right; font-weight: 400; }
  .back-url { left: 68px; top: 197px; width: 428px; height: 43px; font-size: 31px; }
  .back-guarantee { right: 501px; top: 248px; font-size: 34px; }
  .benefits-title { left: 46px; top: 323px; font-size: 19.5px; font-weight: 800; letter-spacing: 0.4px; }
  .back-list { left: 56px; top: 348px; font-size: 16.5px; font-weight: 500; }
  .back-list li { height: 24.7px; gap: 8px; }
  .imprint { right: 46px; top: 411px; font-size: 12.5px; line-height: 16px; text-align: right; font-weight: 500; }
</style>
</head>
<body>

<section class="flyer-side flyer-side--front">
  <svg class="side-bg" viewBox="0 0 973 486" preserveAspectRatio="none">
    <defs>
      <linearGradient id="frontPhoto" x1="0" y1="0" x2="1" y2="1">
        <stop offset="0" stop-color="#dc6a16"/>
        <stop offset="0.55" stop-color="#f29a35"/>
        <stop offset="1" stop-color="#f7b04e"/>
      </linearGradient>
    </defs>
    <rect width="973" height="486" fill="var(--orange)"/>
    <polygon points="0,0 662,0 533,486 0,486" fill="url(#frontPhoto)" role="img" aria-label="Foto: vier fröhliche Frauen in Orange und Weiß mit Getränkebeuteln vor orangefarbenem Hintergrund"/>
  </svg>

  <div class="abs script tagline">Einfacher geht's nicht ...</div>
  <div class="url-box front-url">muehelos-leichter.de</div>
  <div class="abs script front-guarantee">... oder Geld zurück!</div>

  <ul class="checklist front-list">
    <li><svg class="tick" width="20" height="20" viewBox="0 0 20 20"><circle cx="10" cy="10" r="10" fill="#fff"/><path d="M5.5 10.3l3 3 6-6.4" fill="none" stroke="var(--orange)" stroke-width="2.2" stroke-linecap="round" stroke-linejoin="round"/></svg>gesund</li>
    <li><svg class="tick" width="20" height="20" viewBox="0 0 20 20"><circle cx="10" cy="10" r="10" fill="#fff"/><path d="M5.5 10.3l3 3 6-6.4" fill="none" stroke="var(--orange)" stroke-width="2.2" stroke-linecap="round" stroke-linejoin="round"/></svg>nachhaltig</li>
    <li><svg class="tick" width="20" height="20" viewBox="0 0 20 20"><circle cx="10" cy="10" r="10" fill="#fff"/><path d="M5.5 10.3l3 3 6-6.4" fill="none" stroke="var(--orange)" stroke-width="2.2" stroke-linecap="round" stroke-linejoin="round"/></svg>kein Hunger</li>
    <li><svg class="tick" width="20" height="20" viewBox="0 0 20 20"><circle cx="10" cy="10" r="10" fill="#fff"/><path d="M5.5 10.3l3 3 6-6.4" fill="none" stroke="var(--orange)" stroke-width="2.2" stroke-linecap="round" stroke-linejoin="round"/></svg>null Zeitaufwand</li>
    <li><svg class="tick" width="20" height="20" viewBox="0 0 20 20"><circle cx="10" cy="10" r="10" fill="#fff"/><path d="M5.5 10.3l3 3 6-6.4" fill="none" stroke="var(--orange)" stroke-width="2.2" stroke-linecap="round" stroke-linejoin="round"/></svg>für jung und alt</li>
  </ul>

  <div class="abs hotline">Hotline: 0160-51 73 90 8</div>
</section>

<section class="flyer-side flyer-side--back">
  <svg class="side-bg" viewBox="0 0 973 486" preserveAspectRatio="none">
    <defs>
      <linearGradient id="backPhoto" x1="0" y1="0" x2="0" y2="1">
        <stop offset="0" stop-color="#f6ab4c"/>
        <stop offset="0.55" stop-color="#f19a3c"/>
        <stop offset="1" stop-color="#d9681c"/>
      </linearGradient>
    </defs>
    <rect width="973" height="486" fill="var(--orange)"/>
    <polygon points="662,0 973,0 973,486 533,486" fill="url(#backPhoto)" role="img" aria-label="Foto: tanzende Frau mit Getränkebeutel in orangefarbenem Wohnzimmer mit Sofa und Pflanzen"/>
  </svg>

  <p class="abs intro">Verzicht, Sportprogramme, Hungern<br>und Kalorienzählen war gestern ...</p>
  <p class="abs invite">Lernen Sie mit uns die Menschen kennen,<br>die damit bereits echte Erfolge haben.</p>

  <div class="url-box back-url">muehelos-leichter.de</div>
  <div class="abs script back-guarantee">... oder Geld zurück!</div>

  <h2 class="abs benefits-title">Weitere Vorteile:</h2>
  <ul class="checklist back-list">
    <li><svg class="tick" width="19" height="19" viewBox="0 0 20 20"><circle cx="10" cy="10" r="10" fill="#fff"/><path d="M5.5 10.3l3 3 6-6.4" fill="none" stroke="var(--orange)" stroke-width="2.2" stroke-linecap="round" stroke-linejoin="round"/></svg>Senkung des Blutzuckerspiegels und des Blutdrucks</li>
    <li><svg class="tick" width="19" height="19" viewBox="0 0 20 20"><circle cx="10" cy="10" r="10" fill="#fff"/><path d="M5.5 10.3l3 3 6-6.4" fill="none" stroke="var(--orange)" stroke-width="2.2" stroke-linecap="round" stroke-linejoin="round"/></svg>Regulation des Stoffwechsels</li>
    <li><svg class="tick" width="19" height="19" viewBox="0 0 20 20"><circle cx="10" cy="10" r="10" fill="#fff"/><path d="M5.5 10.3l3 3 6-6.4" fill="none" stroke="var(--orange)" stroke-width="2.2" stroke-linecap="round" stroke-linejoin="round"/></svg>Niedriger Insulinspiegel greift Fettreserven an</li>
    <li><svg class="tick" width="19" height="19" viewBox="0 0 20 20"><circle cx="10" cy="10" r="10" fill="#fff"/><path d="M5.5 10.3l3 3 6-6.4" fill="none" stroke="var(--orange)" stroke-width="2.2" stroke-linecap="round" stroke-linejoin="round"/></svg>Rückkehr zu einem normalen Hunger und Sättgungsgefühl</li>
  </ul>

  <p class="abs imprint">Impressum: Lukas Brandl, Lindenweg 7,<br>84999 Musterbach, Tel. 0160-51 73 90 8</p>
</section>

</body>
</html>
```